Homepage Real Estate Agency

I need a web design for a real estate agency in Luxembourg. A short draft for the front page can be found in the project details. (Page 1+2) The main colors of the site should be blue as shown in the project details. (Page 3)
The main target for this site is to promote real estates and a small presentation of the company.

Industry/Entity Type

Real Estate

Requirements
Must have
• On the front page estates are shown in a short preview in small boxes, on the right side is a search. The search is hidden except for the front page. The header has 4 buttons and the logo of the company.

```html
<!DOCTYPE html>
<html lang="fr">
<head>
<meta charset="utf-8">
<title>Cerval Immo – Accueil</title>
<link href="https://fonts.googleapis.com/css2?family=Open+Sans:wght@400;600&family=Pathway+Gothic+One&display=swap" rel="stylesheet">
<style>
:root{
  --navy:#0d3580;
  --blue:#1b57a6;
  --blue-light:#2d6ec0;
  --red:#c8111a;
  --red-text:#c80000;
  --grey-text:#666;
  --panel-grey:#e6e6e6;
  --white:#fff;
  --photo-tone:#a89a86;
  --photo-tone-soft:#b8ab98;
}
*{box-sizing:border-box;margin:0;padding:0}
html,body{width:1059px;height:1200px;overflow:hidden;background:var(--white)}
.page{position:absolute;left:0;top:0;width:1200px;height:1360px;transform:scale(0.8825);transform-origin:0 0;font-family:"Open Sans",sans-serif;color:#333;overflow:hidden}
.abs{position:absolute}
.heading{font-family:"Pathway Gothic One",sans-serif;font-weight:400}
.photo{background:var(--photo-tone)}

/* header */
.top-strip{left:0;top:0;width:1200px;height:10px;background:var(--navy)}
.header{left:0;top:10px;width:1200px;height:153px;background:linear-gradient(#dcdcdc,#f4f4f4 45%,#fff)}
.logo-tab{left:120px;top:0;width:186px;height:160px;background:linear-gradient(#fff,#dedede);border-radius:0 0 30px 30px;box-shadow:0 2px 6px rgba(0,0,0,.25);display:flex;flex-direction:column;align-items:center;justify-content:center;gap:8px}
.logo-dot{width:56px;height:56px;border-radius:50%;background:var(--navy)}
.logo-name{font-family:"Open Sans",sans-serif;font-weight:600;font-size:17px;color:var(--navy)}
.account{right:124px;top:19px;font-size:12px;color:var(--grey-text)}
.main-nav{left:538px;top:56px;display:flex;font-family:"Pathway Gothic One",sans-serif;font-size:27px}
.main-nav a{display:block;height:38px;line-height:38px;text-decoration:none;color:#555;margin-right:26px}
.main-nav a.active{background:linear-gradient(var(--blue-light),var(--navy));color:var(--white);padding:0 21px;border-radius:4px;margin-right:8px}

/* slider */
.hero-band{left:0;top:163px;width:1200px;height:310px;background:linear-gradient(90deg,#0e3f8f,#2a67b7 15%,#1f5bab 50%,#2a67b7 85%,#0e3f8f)}
.slider-frame{left:134px;top:174px;width:932px;height:307px;background:var(--white);box-shadow:0 12px 10px -8px rgba(0,0,0,.25)}
.slider-photo{left:143px;top:181px;width:914px;height:293px;background:var(--photo-tone-soft)}
.slider-arrow{top:288px;width:56px;height:88px;background:linear-gradient(#2b63b5,#0e3a86)}
.slider-arrow.prev{left:134px;border-radius:0 44px 44px 0}
.slider-arrow.next{left:1010px;border-radius:44px 0 0 44px}
.slider-arrow svg{position:absolute;top:32px}

/* panels */
.blue-panel{background:linear-gradient(90deg,#0e3e8d,#1f5cab 70%,#2a67b7)}
.panel-title{position:absolute;left:14px;top:10px;font-size:29px;color:var(--white)}
.panel-rule{position:absolute;left:12px;right:12px;top:44px;border-top:1px dotted #7fa2d4}
.featured{left:120px;top:516px;width:659px;height:375px}
.offer{position:absolute;top:60px;width:188px;color:var(--white)}
.photo-frame{width:188px;height:168px;border:2px solid var(--white);padding:7px;background:var(--white);box-shadow:inset 0 0 0 1px #0e3e8d}
.photo-frame>div{width:100%;height:100%}
.offer-title{margin-top:8px;font-size:14px;line-height:21px;padding-left:4px}
.offer-price{font-size:14px;line-height:21px;padding-left:4px}
.offer-price span{color:#ff1a1a}
.offer-desc{margin-top:6px;font-size:12px;line-height:15.5px;padding-left:4px}
.details-btn{margin:12px 0 0 4px;width:98px;height:26px;border:2px solid var(--white);border-radius:3px 13px 13px 3px;background:linear-gradient(#e02a2a,#a80c10);color:var(--white);font-size:12px;line-height:22px;padding-left:26px;position:relative}
.details-btn::after{content:"";position:absolute;right:6px;top:6px;width:9px;height:9px;border-radius:50%;background:var(--white)}

.search-box{left:792px;top:516px;width:288px;height:375px;border:1px solid #c9c9c9;background:var(--white)}
.search-inner{position:absolute;left:4px;top:4px;width:278px;height:364px;background:var(--panel-grey)}
.search-title{position:absolute;left:11px;top:8px;font-size:27px;color:#666}
.search-rule{position:absolute;left:10px;right:10px;top:43px;border-top:1px dotted #bbb}
.field-label{position:absolute;font-size:12.5px;color:#555}
.field{position:absolute;height:21px;background:var(--white);border:1px solid #c4c4c4}
.select{position:absolute;height:21px;background:var(--white);border:1px solid #c4c4c4;font-size:12px;color:#666;line-height:19px;padding-left:8px}
.select::after{content:"";position:absolute;right:2px;top:2px;width:15px;height:15px;background:linear-gradient(#6cc0ef,#2c8fd0);border-radius:2px}
.select svg{position:absolute;right:5px;top:7px;z-index:1}
.search-btn{position:absolute;left:132px;top:300px;width:138px;height:33px;border-radius:4px 17px 17px 4px;background:linear-gradient(#e52a2a,#b00d12);color:var(--white);font-size:13px;line-height:32px;padding-left:8px;white-space:nowrap}
.search-btn::after{content:"";position:absolute;right:5px;top:8px;width:16px;height:16px;border-radius:50%;background:#bbb}
.search-note{position:absolute;left:12px;top:335px;font-size:10.5px;line-height:13px;color:#666}

.gallery{left:120px;top:915px;width:960px;height:255px}
.thumb{position:absolute;top:76px;width:157px;height:140px;border:1px solid var(--white);padding:7px;background:var(--white)}
.thumb>div{width:100%;height:100%}

/* footer */
.footer-strip{left:0;top:1180px;width:1200px;height:10px;background:var(--navy)}
.footer{left:0;top:1190px;width:1200px;height:170px;background:linear-gradient(#d6d6d6,#f3f3f3 40%,#fff)}
.foot-heading{font-size:26px;color:#666}
.locality-col{top:1235px;width:120px}
.locality-col h3{font-weight:400;font-size:14.5px;color:var(--red-text);margin-bottom:6px}
.locality-col a,.foot-links a{display:block;text-decoration:none;color:#777;font-size:12.5px;line-height:16.2px}
.foot-divider{left:762px;top:1200px;width:1px;height:145px;background:#bbb}
.foot-links{left:783px;top:1224px}
.social{top:1231px;width:32px;height:32px;border-radius:5px;background:linear-gradient(#3b77c8,#18478f)}
.copyright{left:784px;top:1340px;font-size:11px;color:var(--red-text)}
</style>
</head>
<body>
<div class="page">
  <div class="abs top-strip"></div>
  <header class="abs header"></header>
  <div class="abs logo-tab">
    <div class="logo-dot"></div>
    <div class="logo-name">Cerval Immo</div>
  </div>
  <div class="abs account">Login&nbsp; | &nbsp;Signup</div>
  <nav class="abs main-nav">
    <a class="active" href="#">HOME</a>
    <a href="#">A VENDRE</a>
    <a href="#">CONSTRUCTION</a>
    <a href="#">LOCATION</a>
    <a href="#">CHERCHONS</a>
  </nav>

  <section class="abs hero-band"></section>
  <div class="abs slider-frame"></div>
  <div class="abs slider-photo" role="img" aria-label="Photo of a large two-storey family house with porch"></div>
  <div class="abs slider-arrow prev"><svg width="24" height="24" viewBox="0 0 24 24" style="left:8px"><path d="M16 3 L6 12 L16 21" fill="none" stroke="#d01a22" stroke-width="4"/></svg></div>
  <div class="abs slider-arrow next"><svg width="24" height="24" viewBox="0 0 24 24" style="left:26px"><path d="M8 3 L18 12 L8 21" fill="none" stroke="#d01a22" stroke-width="4"/></svg></div>

  <section class="abs blue-panel featured">
    <h2 class="panel-title heading">Featured Offers</h2>
    <div class="panel-rule"></div>
    <div class="offer" style="left:11px">
      <div class="photo-frame"><div class="photo" role="img" aria-label="Photo of a bungalow with white fence"></div></div>
      <p class="offer-title">sample text</p>
      <p class="offer-price">Price: <span>0000000</span></p>
      <p class="offer-desc">sample text sample text<br>sample text sample text<br>sample text sample text</p>
      <div class="details-btn">Details</div>
    </div>
    <div class="offer" style="left:236px">
      <div class="photo-frame"><div class="photo" role="img" aria-label="Photo of a yellow house at dusk"></div></div>
      <p class="offer-title">sample text</p>
      <p class="offer-price">Price: <span>0000000</span></p>
      <p class="offer-desc">sample text sample text<br>sample text sample text<br>sample text sample text</p>
      <div class="details-btn">Details</div>
    </div>
    <div class="offer" style="left:460px">
      <div class="photo-frame"><div class="photo" role="img" aria-label="Photo of a cottage with garden"></div></div>
      <p class="offer-title">sample text</p>
      <p class="offer-price">Price: <span>0000000</span></p>
      <p class="offer-desc">sample text sample text<br>sample text sample text<br>sample text sample text</p>
      <div class="details-btn">Details</div>
    </div>
  </section>

  <aside class="abs search-box">
    <div class="search-inner">
      <h2 class="search-title heading">Find Your Property</h2>
      <div class="search-rule"></div>
      <span class="field-label" style="left:11px;top:49px">City:</span>
      <span class="field-label" style="left:156px;top:49px">State:</span>
      <div class="field" style="left:11px;top:69px;width:113px"></div>
      <div class="field" style="left:156px;top:69px;width:113px"></div>
      <span class="field-label" style="left:13px;top:99px">Zip:</span>
      <span class="field-label" style="left:156px;top:99px">Country:</span>
      <div class="field" style="left:13px;top:119px;width:113px"></div>
      <div class="field" style="left:156px;top:119px;width:113px"></div>
      <span class="field-label" style="left:14px;top:148px">Price Range:</span>
      <div class="select" style="left:14px;top:168px;width:111px">Max<svg width="8" height="5" viewBox="0 0 8 5"><path d="M0 0 L8 0 L4 5Z" fill="#fff"/></svg></div>
      <span class="field-label" style="left:131px;top:172px">To:</span>
      <div class="select" style="left:156px;top:168px;width:113px">Min<svg width="8" height="5" viewBox="0 0 8 5"><path d="M0 0 L8 0 L4 5Z" fill="#fff"/></svg></div>
      <span class="field-label" style="left:14px;top:200px">Bedroom:</span>
      <div class="select" style="left:14px;top:220px;width:255px"><svg width="8" height="5" viewBox="0 0 8 5"><path d="M0 0 L8 0 L4 5Z" fill="#fff"/></svg></div>
      <span class="field-label" style="left:14px;top:249px">Bathroom:</span>
      <div class="select" style="left:14px;top:269px;width:255px"><svg width="8" height="5" viewBox="0 0 8 5"><path d="M0 0 L8 0 L4 5Z" fill="#fff"/></svg></div>
      <div class="search-btn">Search Property</div>
      <p class="search-note">Know exactly what you want?<br>Advanced search</p>
    </div>
  </aside>

  <section class="abs blue-panel gallery">
    <h2 class="panel-title heading">Project Gallery</h2>
    <div class="panel-rule"></div>
    <div class="thumb" style="left:11px"><div class="photo" role="img" aria-label="Photo of a bungalow with white fence"></div></div>
    <div class="thumb" style="left:203px"><div class="photo" role="img" aria-label="Photo of a white gabled house"></div></div>
    <div class="thumb" style="left:402px"><div class="photo" role="img" aria-label="Photo of a brick cottage with chimney"></div></div>
    <div class="thumb" style="left:595px"><div class="photo" role="img" aria-label="Photo of a row of suburban houses"></div></div>
    <div class="thumb" style="left:788px"><div class="photo" role="img" aria-label="Photo of a large beige family house"></div></div>
  </section>

  <div class="abs footer-strip"></div>
  <footer class="abs footer"></footer>
  <h2 class="abs heading foot-heading" style="left:122px;top:1192px">Browse Propery by Locality</h2>
  <div class="abs locality-col" style="left:122px"><h3>Country Name</h3><a href="#">sample link</a><a href="#">sample link</a><a href="#">sample link</a><a href="#">sample link</a><a href="#">sample link</a></div>
  <div class="abs locality-col" style="left:259px"><h3>Country Name</h3><a href="#">sample link</a><a href="#">sample link</a><a href="#">sample link</a><a href="#">sample link</a><a href="#">sample link</a></div>
  <div class="abs locality-col" style="left:391px"><h3>Country Name</h3><a href="#">sample link</a><a href="#">sample link</a><a href="#">sample link</a><a href="#">sample link</a><a href="#">sample link</a></div>
  <div class="abs locality-col" style="left:517px"><h3>Country Name</h3><a href="#">sample link</a><a href="#">sample link</a><a href="#">sample link</a><a href="#">sample link</a><a href="#">sample link</a></div>
  <div class="abs locality-col" style="left:650px"><h3>Country Name</h3><a href="#">sample link</a><a href="#">sample link</a><a href="#">sample link</a><a href="#">sample link</a><a href="#">sample link</a></div>
  <div class="abs foot-divider"></div>
  <h2 class="abs heading foot-heading" style="left:783px;top:1192px">Links</h2>
  <nav class="abs foot-links"><a href="#">Home</a><a href="#">About Us</a><a href="#">A Vendre</a><a href="#">Construction</a><a href="#">Location</a><a href="#">Cherchons</a><a href="#">Contact Us</a></nav>
  <h2 class="abs heading foot-heading" style="left:949px;top:1192px">Follow Us</h2>
  <div class="abs social" style="left:948px"></div>
  <div class="abs social" style="left:990px"></div>
  <div class="abs social" style="left:1031px"></div>
  <p class="abs copyright">© copyright 2012 by Real estate all rights reserved.</p>
</div>
</body>
</html>
```